volnex needs updated company presentation for perspective principals

We are looking to update our current company overview presentation that we use for giving new and prospective principals (companies we see for) an overview of our company and our capabilities. We have a PowerPoint presentation but would like to give it a more professional and updated look. There are some modification we'd like to incorporate into the new presentation, but that can be added later.
We will also be looking at using this look to update our website and some additional promotion literature for the near future ( Brochures, Mailers....)
Updates

On the territory overview. I need to increase the state view to include Missouri, Iowa, Kansas, Nebraska, Minnesota and Tennessee. This is the first project we've worked on, so please let me know what additional information is required or makes this process go smoother.

Industry/Entity Type

Chemical Product

Font styles to use
Serif

Colors
ec1f27
000000

Requirements
Must have
• Company History, Territory overview, Industries Served, Principal Represented, Employee overview, Historic Performance

```html
<!DOCTYPE html>
<html lang="en">
<head>
<meta charset="utf-8">
<title>volnex company presentation</title>
<link rel="stylesheet" href="https://fonts.googleapis.com/css2?family=Ubuntu:wght@400;500;700&family=Lato:wght@400;700&family=Roboto+Condensed:wght@700&display=swap">
<style>
  :root {
    --red: #c00a16;
    --red-soft: #d0353d;
    --black: #1a1a1a;
    --ink: #333333;
    --muted: #666666;
    --grey: #8a8a8a;
    --grey-light: #eeeeee;
    --grey-mid: #e2e2e2;
    --rule: #e9e9e9;
    --white: #ffffff;
    --stage: #767676;
  }
  * { margin: 0; padding: 0; box-sizing: border-box; }
  html, body { width: 1200px; height: 1200px; overflow: hidden; }
  body {
    background: radial-gradient(circle at 50% 40%, #8c8c8c 0%, var(--stage) 60%, #6a6a6a 100%);
    position: relative;
    font-family: "Lato", sans-serif;
    color: var(--ink);
  }
  .slide {
    position: absolute;
    width: 517px; height: 379px;
    background: var(--white);
    overflow: hidden;
    transform: scale(0.8);
    transform-origin: 0 0;
    box-shadow: 0 14px 22px rgba(0,0,0,0.35);
  }
  .col-left { left: 170px; }
  .col-right { left: 636px; }
  .row-1 { top: 118px; }
  .row-2 { top: 464px; }
  .row-3 { top: 810px; }
  .abs { position: absolute; }
  .shapes { position: absolute; left: 0; top: 0; }

  .header-bar {
    position: absolute; left: 0; top: 0; width: 517px; height: 72px;
    background: var(--red);
  }
  .slide-title {
    position: absolute; left: 15px; top: 18px;
    font-family: "Ubuntu", sans-serif; font-weight: 400; font-size: 26px;
    color: var(--white); white-space: nowrap;
  }
  .slide-title.dark { color: var(--black); top: 12px; }
  .badge {
    position: absolute; width: 46px; height: 46px; border-radius: 50%;
    background: var(--white); border: 5px solid var(--red);
    box-shadow: inset 0 0 0 3px var(--white), inset 0 0 0 5px var(--red);
  }
  .badge.grey { border-color: #b5b5b5; box-shadow: inset 0 0 0 3px var(--white), inset 0 0 0 5px #b5b5b5; }
  .wordmark {
    position: absolute;
    font-family: "Ubuntu", sans-serif; font-weight: 700;
    color: var(--red); letter-spacing: -0.5px; white-space: nowrap; line-height: 1;
  }
  .wordmark.small { font-size: 23px; }
  .fine {
    position: absolute; font-size: 6.5px; line-height: 1.4; color: var(--muted);
  }
  .band-bottom { position: absolute; left: 0; bottom: 0; width: 517px; height: 14px; background: var(--red); }

  /* cover */
  .cover-glow {
    position: absolute; left: 0; top: 0; width: 198px; height: 228px;
    background: linear-gradient(135deg, #eef2f4 0%, #cfe0e6 60%, #c5d8df 100%);
  }
  .cover-brand { left: 238px; top: 104px; font-size: 42px; }
  .tagline {
    position: absolute; left: 240px; top: 257px; width: 237px; text-align: center;
    font-family: "Roboto Condensed", sans-serif; font-weight: 700; font-size: 14px;
    color: var(--white);
  }
  .cover-badge { left: 34px; top: 234px; width: 66px; height: 66px; border-width: 6px; }

  /* company history */
  .icon-disc {
    position: absolute; width: 68px; height: 68px; border-radius: 50%;
    background: var(--red); display: flex; align-items: center; justify-content: center;
    color: var(--white);
  }
  .sample-title {
    position: absolute; top: 646px; width: 160px; text-align: center;
    font-family: "Lato", sans-serif; font-size: 13px; color: #777;
  }
  .history-panel { position: absolute; top: 240px; height: 122px; width: 169px; background: var(--grey-light); }
  .history-panel.mid { background: var(--grey-mid); }
  .history-panel p { position: absolute; left: 28px; width: 115px; font-size: 6.5px; line-height: 1.4; color: var(--muted); }

  /* industries photo circle */
  .photo-disc {
    position: absolute; left: 190px; top: 81px; width: 136px; height: 136px; border-radius: 50%;
    background: linear-gradient(135deg, #d8f0f2 0%, #c4e2e6 45%, #e6eef0 100%);
    display: flex; align-items: center; justify-content: center;
    font-size: 13px; color: var(--white);
  }
  .text-title {
    position: absolute; left: 0; top: 230px; width: 517px; text-align: center;
    font-size: 20px; color: #777;
  }

  /* industries list */
  .bullet-item { position: absolute; font-size: 8.5px; line-height: 1.35; color: var(--muted); padding-left: 10px; }
  .bullet-item::before {
    content: ""; position: absolute; left: 0; top: 3px; width: 4px; height: 4px; border-radius: 50%; background: var(--red);
  }
  .bullet-item.faint::before { background: #e4e4e4; }
  .divider { position: absolute; left: 333px; top: 110px; width: 2px; height: 140px; background: var(--rule); }
  .column-copy { position: absolute; left: 372px; top: 107px; width: 115px; font-size: 8.5px; line-height: 1.35; color: var(--muted); }

  /* industries photo banner */
  .city-photo {
    position: absolute; left: 0; top: 108px; width: 517px; height: 118px;
    background: linear-gradient(180deg, #9ec3e0 0%, #d5e3ee 55%, #a9b4bb 78%, #7d8a92 100%);
  }
  .feature-bar { position: absolute; left: 0; top: 226px; width: 517px; height: 40px; display: flex; }
  .feature-bar .cell { flex: 1; display: flex; align-items: center; justify-content: center; }
  .feature-bar .cell.red { background: var(--red-soft); }
  .feature-bar .cell.grey { background: var(--grey); }
  .feature-copy { position: absolute; top: 266px; left: 0; width: 517px; height: 92px; background: var(--grey-light); }
  .feature-copy p { position: absolute; top: 16px; width: 90px; font-size: 8.5px; line-height: 1.35; color: var(--muted); }
</style>
</head>
<body>

<!-- Cover -->
<section class="slide col-left row-1">
  <div class="cover-glow"></div>
  <svg class="shapes" width="517" height="379" viewBox="0 0 517 379">
    <rect x="0" y="228" width="159" height="71" fill="var(--red)"/>
    <polygon points="159,228 198,182 198,259 159,299" fill="#8f8f8f"/>
    <polygon points="198,182 237,228 198,228" fill="var(--red-soft)"/>
    <polygon points="198,228 517,228 517,299 237,299 198,259" fill="var(--red)"/>
  </svg>
  <div class="wordmark cover-brand">volnex</div>
  <div class="badge cover-badge"></div>
  <div class="tagline">Representing the World's Best</div>
  <p class="fine" style="left:32px; top:327px; width:460px;">We represent leading chemical manufacturers across the Midwest, offering technical sales support, market insight and trusted distribution relationships.</p>
</section>

<!-- Territory overview -->
<section class="slide col-right row-1">
  <div class="header-bar"></div>
  <h2 class="slide-title">Territory overview</h2>
  <div class="badge" style="left:455px; top:14px;"></div>
  <div class="wordmark small" style="left:23px; top:76px;">volnex</div>
  <svg class="shapes" width="517" height="379" viewBox="0 0 517 379">
    <g stroke="var(--rule)" stroke-width="1.5">
      <line x1="0" y1="117" x2="517" y2="117"/>
      <line x1="0" y1="140" x2="517" y2="140"/>
      <line x1="0" y1="162" x2="517" y2="162"/>
      <line x1="0" y1="185" x2="517" y2="185"/>
      <line x1="0" y1="209" x2="517" y2="209"/>
      <line x1="0" y1="232" x2="517" y2="232"/>
      <line x1="0" y1="255" x2="517" y2="255"/>
      <line x1="0" y1="278" x2="517" y2="278"/>
      <line x1="0" y1="299" x2="517" y2="299"/>
    </g>
    <rect x="38" y="155" width="4" height="144" fill="#6e6e6e"/>
    <polygon points="60,299 139,159 197,299" fill="var(--red)"/>
    <polygon points="175,299 227,207 280,299" fill="#8f8f8f"/>
    <polygon points="275,299 369,207 475,299" fill="var(--red-soft)"/>
  </svg>
  <p class="fine" style="left:30px; top:328px; width:460px;">Our territory spans twelve states, including Missouri, Iowa, Kansas, Nebraska, Minnesota and Tennessee, served by dedicated field representatives.</p>
</section>

<!-- Company History -->
<section class="slide col-left row-2">
  <div class="header-bar"></div>
  <h2 class="slide-title" style="left:19px;">Company History</h2>
  <div class="badge" style="left:460px; top:14px;"></div>
  <div class="wordmark small" style="left:15px; top:78px;">volnex</div>

  <div class="icon-disc" style="left:38px; top:114px;">
    <svg width="32" height="32" viewBox="0 0 32 32" fill="none" stroke="#fff" stroke-width="2"><circle cx="19" cy="12" r="8"/><line x1="13" y1="18" x2="5" y2="27"/></svg>
  </div>
  <div class="icon-disc" style="left:223px; top:114px; font-family:'Lato',sans-serif; font-size:30px;">$</div>
  <div class="icon-disc" style="left:398px; top:114px;">
    <svg width="26" height="26" viewBox="0 0 26 26" fill="#fff"><rect x="4" y="13" width="4" height="9"/><rect x="11" y="6" width="4" height="16"/><rect x="18" y="16" width="4" height="6"/></svg>
  </div>

  <div class="sample-title" style="left:-11px; top:214px;">SAMPLE TITLE</div>
  <div class="sample-title" style="left:170px; top:214px;">SAMPLE TITLE</div>
  <div class="sample-title" style="left:342px; top:214px;">SAMPLE TITLE</div>

  <div class="history-panel" style="left:0;"><p style="top:36px;">Founded as a regional agency with a focus on chemicals.</p></div>
  <div class="history-panel mid" style="left:169px;"><p style="top:32px;">Steady growth brought new principals, broader product lines and a larger sales team serving customers across several neighbouring states each year.</p></div>
  <div class="history-panel" style="left:338px; width:179px;"><p style="top:36px; left:32px;">Today we represent global producers with local service, technical knowledge and long customer ties.</p></div>
</section>

<!-- Industries Served: feature -->
<section class="slide col-right row-2">
  <h2 class="slide-title dark" style="left:13px; top:14px;">Industries Served</h2>
  <div class="badge grey" style="left:449px; top:14px;"></div>
  <div class="wordmark small" style="left:14px; top:60px;">volnex</div>
  <div class="photo-disc" role="img" aria-label="Round photo of an industry served">PHOTO</div>
  <div class="text-title">TEXT TITLE</div>
  <p class="fine" style="left:92px; top:271px; width:333px; text-align:center;">We serve coatings, plastics, water treatment, agriculture, food processing and industrial cleaning markets. Our team matches each customer with the right product and brings practical technical support from sampling to supply.</p>
  <div class="band-bottom"></div>
</section>

<!-- Industries Served: chart -->
<section class="slide col-left row-3">
  <h2 class="slide-title dark" style="left:21px; top:16px;">Industries Served</h2>
  <div class="badge grey" style="left:456px; top:16px;"></div>
  <div class="wordmark small" style="left:22px; top:56px;">volnex</div>
  <svg class="shapes" width="517" height="379" viewBox="0 0 517 379">
    <defs>
      <linearGradient id="core-fill" x1="0" y1="0" x2="1" y2="1">
        <stop offset="0" stop-color="#d3eef1"/>
        <stop offset="1" stop-color="#e7eaec"/>
      </linearGradient>
    </defs>
    <circle cx="106" cy="178" r="58" fill="none" stroke="#efefef" stroke-width="13"/>
    <circle cx="106" cy="178" r="58" fill="none" stroke="var(--red)" stroke-width="13"
            stroke-dasharray="200 165" transform="rotate(-100 106 178)"/>
    <circle cx="106" cy="178" r="58" fill="none" stroke="var(--red-soft)" stroke-width="13"
            stroke-dasharray="42 323" transform="rotate(99 106 178)"/>
    <circle cx="106" cy="178" r="35" fill="url(#core-fill)"/>
    <circle cx="136" cy="128" r="2.5" fill="#fff"/>
    <circle cx="145" cy="222" r="2.5" fill="#fff"/>
    <circle cx="58" cy="213" r="2.5" fill="#fff"/>
  </svg>
  <p class="bullet-item" style="left:187px; top:109px; width:95px;">Coatings and adhesives for industrial manufacturers</p>
  <p class="bullet-item" style="left:187px; top:228px; width:115px;">Water treatment and municipal process chemicals</p>
  <p class="bullet-item faint" style="left:47px; top:271px; width:90px;">Agriculture and food processing</p>
  <div class="divider"></div>
  <p class="column-copy">We work with manufacturers in a wide range of industries, supplying specialty and commodity chemicals. Our representatives understand each market and help customers solve formulation, cost and supply challenges with proven products.</p>
  <div class="band-bottom"></div>
</section>

<!-- Industries Served: banner -->
<section class="slide col-right row-3">
  <div class="header-bar"></div>
  <h2 class="slide-title" style="left:8px; top:22px;">Industries Served</h2>
  <div class="badge" style="left:460px; top:16px;"></div>
  <div class="wordmark small" style="left:13px; top:77px;">volnex</div>
  <div class="city-photo" role="img" aria-label="Photo of a city skyline under a bright sky"></div>
  <div class="feature-bar">
    <div class="cell red">
      <svg width="24" height="24" viewBox="0 0 24 24" fill="none" stroke="#fff" stroke-width="1.6"><circle cx="12" cy="8" r="4.5"/><path d="M3 22 v-2 a6 6 0 0 1 6 -6 h6 a6 6 0 0 1 6 6 v2 z"/></svg>
    </div>
    <div class="cell grey">
      <svg width="28" height="24" viewBox="0 0 28 24" fill="none" stroke="#fff" stroke-width="1.6"><polyline points="2,2 2,22 26,22"/><polyline points="5,18 11,11 15,15 24,5"/></svg>
    </div>
    <div class="cell red">
      <svg width="20" height="24" viewBox="0 0 20 24" fill="none" stroke="#fff" stroke-width="1.6"><circle cx="10" cy="8" r="6"/><line x1="10" y1="14" x2="10" y2="22"/><line x1="6" y1="18" x2="14" y2="18"/></svg>
    </div>
    <div class="cell grey">
      <svg width="24" height="24" viewBox="0 0 24 24" fill="none" stroke="#fff" stroke-width="1.6"><circle cx="12" cy="12" r="10"/><polyline points="14,7 9,12 14,17"/></svg>
    </div>
  </div>
  <div class="feature-copy">
    <p style="left:23px;">Experienced people focused on long term customer partnerships.</p>
    <p style="left:155px;">Consistent sales growth across our territory, year after year, with trusted principals.</p>
    <p style="left:286px;">New ideas and technical insight for every application.</p>
    <p style="left:418px;">Fast response and reliable delivery across the region.</p>
  </div>
</section>

</body>
</html>
```